We are looking for a Flyer we will send through the mail for residents of Apartment Buildings

We are a laundry service doing pickup and delivery for the Manhattan Area.
We offer next day delivery on all laundry orders.
we want to send out a flyer to buildings for unbelievable promotion:

50% your first order (coupon code ROVK50)
2nd order FREE! (up to $50)
FREE pickup and delivery
FREE next day service
FREE Kestrel and Plumeo
schedule now on www.brimfold.com!

We offer the cleanest and brightest laundry in the city!
Attached is our logo plus some icons to use

Target Market(s)

females ages 24-40

Industry/Entity Type

Apartment

Font styles to use
Other font styles liked:
• habraba

Requirements
Must have
• modern and clean look
• our logo
• BRIGHT COLORS
• Size of flyer will be 8.52 x 5.47
• Logo font: Harabara
• Slogan font: Swiss 721 Light Extended BT
• Dark blue: C 100 M 88 Y 0 K 0
• Light blue: C 85 M 50 Y 0 K 0
• Orange: C 0 M 80 Y 95 K 0
• Violet: C 85 M 100 Y 0 K 0
Should not have
• we dont want to be too busy

```html
<!DOCTYPE html>
<html lang="en">
<head>
<meta charset="utf-8">
<title>brimfold.com flyer</title>
<link rel="stylesheet" href="https://fonts.googleapis.com/css2?family=Open+Sans:wght@700;800&family=PT+Sans+Narrow:wght@700&family=Montserrat:wght@300;400;700&display=swap">
<style>
  :root {
    --dark-blue: #213f99;
    --light-blue: #1a75c6;
    --orange: #f05a28;
    --paper-top: #ffffff;
    --paper-bottom: #dcebf8;
    --ink-grey: #6d6d6d;
    --badge-blue: #6fa7d3;
    --badge-sand: #e8c98a;
    --badge-dark: #222222;
    --white: #ffffff;
  }
  * { margin: 0; padding: 0; box-sizing: border-box; }
  html, body { width: 885px; height: 1200px; overflow: hidden; background: #ffffff; }
  .flyer {
    position: relative;
    width: 885px;
    height: 1200px;
    overflow: hidden;
    background: linear-gradient(90deg, var(--paper-bottom) 0%, #f4f8fc 60%, var(--paper-top) 100%);
    font-family: "Open Sans", Arial, sans-serif;
  }
  .flyer-shapes { position: absolute; inset: 0; }
  .headline {
    position: absolute; top: 22px; left: 0; width: 885px;
    text-align: center; color: var(--white);
    font-weight: 700; font-size: 40px; line-height: 48px; letter-spacing: -0.5px;
  }
  .perks { position: absolute; left: 27px; top: 312px; list-style: none; }
  .perk {
    display: flex; align-items: center; height: 55px;
    font-family: "PT Sans Narrow", "Arial Narrow", sans-serif;
    font-weight: 700; font-size: 28px; color: var(--dark-blue);
  }
  .perk svg { width: 36px; height: 34px; margin-right: 18px; }
  .price {
    position: absolute; left: 120px; top: 476px; width: 160px; text-align: center;
    font-family: "PT Sans Narrow", "Arial Narrow", sans-serif;
    font-weight: 700; font-size: 36px; color: var(--orange);
  }
  .coupon {
    position: absolute; left: 404px; top: 258px; width: 451px; height: 259px;
    color: var(--white); font-family: "Montserrat", Arial, sans-serif; text-align: center;
  }
  .care-icons { position: absolute; top: 30px; left: 0; width: 100%; display: flex; justify-content: center; gap: 10px; }
  .care-icons svg { width: 34px; height: 28px; }
  .coupon-offer { position: absolute; top: 58px; left: 0; width: 100%; font-size: 25px; font-weight: 400; }
  .coupon-offer b { font-size: 48px; font-weight: 700; margin-right: 6px; }
  .coupon-code {
    position: absolute; top: 118px; left: 31px; width: 387px; height: 44px;
    background: var(--white); color: var(--ink-grey); font-size: 26px; line-height: 44px;
  }
  .coupon-free { position: absolute; top: 170px; left: 0; width: 100%; font-size: 33px; font-weight: 700; }
  .coupon-cap { position: absolute; top: 214px; left: 0; width: 100%; font-size: 22px; font-weight: 400; }
  .partner-badges { position: absolute; top: 552px; left: 440px; display: flex; gap: 40px; align-items: center; }
  .badge { width: 82px; height: 82px; }
  .badge-round-blue { border-radius: 50%; background: var(--badge-blue); }
  .badge-round-sand { border-radius: 50%; background: var(--badge-sand); }
  .badge-square { width: 86px; height: 70px; border-radius: 10px; background: var(--badge-dark); }
  .call-to-action {
    position: absolute; top: 662px; left: 0; width: 885px; text-align: center;
    color: var(--orange); font-weight: 700; font-size: 32px; line-height: 42px; letter-spacing: -0.3px;
  }
  .basket-art {
    position: absolute; left: 300px; top: 782px; width: 280px; height: 160px;
    border-radius: 40px 40px 60px 60px;
    background: linear-gradient(180deg, #e84a6f 0%, #2f8fd8 45%, #2a9b4a 75%, #d8333b 100%);
  }
  .brand-name {
    position: absolute; top: 952px; left: 0; width: 885px; text-align: center;
    color: var(--light-blue); font-weight: 700; font-size: 52px; letter-spacing: -1px; line-height: 62px;
  }
  .slogan {
    position: absolute; top: 1020px; left: 0; width: 885px; text-align: center;
    color: var(--orange); font-family: "Montserrat", Arial, sans-serif; font-weight: 300;
    font-size: 19px; line-height: 24px; letter-spacing: 1.5px;
  }
  .footer-line {
    position: absolute; top: 1124px; left: 0; width: 885px; text-align: center;
    color: var(--white); font-weight: 700; font-size: 34px; letter-spacing: -0.5px;
  }
</style>
</head>
<body>
<main class="flyer">
  <svg class="flyer-shapes" width="885" height="1200" viewBox="0 0 885 1200" aria-hidden="true">
    <path d="M0 0 H885 V170 C700 215 500 170 300 185 C150 195 60 215 0 240 Z" fill="var(--light-blue)"/>
    <path d="M0 246 C120 205 300 190 480 198 C650 206 780 200 885 178 V204 C760 234 620 228 470 220 C300 212 130 230 0 276 Z" fill="var(--dark-blue)"/>
    <path d="M0 1068 C200 1036 420 1062 600 1052 C720 1045 820 1032 885 1012 V1040 C780 1066 640 1076 480 1073 C300 1069 150 1062 0 1088 Z" fill="var(--dark-blue)"/>
    <path d="M0 1094 C160 1068 330 1082 520 1084 C700 1086 800 1072 885 1052 V1200 H0 Z" fill="var(--light-blue)"/>
    <g>
      <path d="M420 258 H512 L471 205 L606 258 H839 Q855 258 855 274 V501 Q855 517 839 517 H420 Q404 517 404 501 V274 Q404 258 420 258 Z" fill="#b9c7d6" transform="translate(3 5)"/>
      <path d="M420 258 H512 L471 205 L606 258 H839 Q855 258 855 274 V501 Q855 517 839 517 H420 Q404 517 404 501 V274 Q404 258 420 258 Z" fill="var(--orange)"/>
      <path d="M426 268 H524 L488 222 L600 268 H835 Q845 268 845 278 V497 Q845 507 835 507 H424 Q414 507 414 497 V278 Q414 268 426 268 Z" fill="none" stroke="var(--white)" stroke-width="1.5" stroke-dasharray="6 4"/>
    </g>
  </svg>

  <h1 class="headline">WE OFFER THE CLEANEST AND<br>BRIGHTEST LAUNDRY IN THE CITY!</h1>

  <ul class="perks">
    <li class="perk"><svg viewBox="0 0 36 34"><rect x="2" y="6" width="26" height="26" rx="4" fill="none" stroke="var(--orange)" stroke-width="3"/><path d="M8 17 L15 24 L33 3" fill="none" stroke="var(--orange)" stroke-width="3.5"/></svg>FREE pickup and delivery</li>
    <li class="perk"><svg viewBox="0 0 36 34"><rect x="2" y="6" width="26" height="26" rx="4" fill="none" stroke="var(--orange)" stroke-width="3"/><path d="M8 17 L15 24 L33 3" fill="none" stroke="var(--orange)" stroke-width="3.5"/></svg>FREE next day service</li>
    <li class="perk"><svg viewBox="0 0 36 34"><rect x="2" y="6" width="26" height="26" rx="4" fill="none" stroke="var(--orange)" stroke-width="3"/><path d="M8 17 L15 24 L33 3" fill="none" stroke="var(--orange)" stroke-width="3.5"/></svg>FREE Kestrel and Plumeo</li>
  </ul>
  <p class="price">$1.10 a lb</p>

  <section class="coupon">
    <div class="care-icons" aria-hidden="true">
      <svg viewBox="0 0 34 28"><path d="M4 6 L8 24 H26 L30 6" fill="none" stroke="#fff" stroke-width="1.5"/><path d="M5 4 L29 26 M29 4 L5 26" stroke="#fff" stroke-width="1.5"/></svg>
      <svg viewBox="0 0 34 28"><path d="M4 6 L8 24 H26 L30 6" fill="none" stroke="#fff" stroke-width="1.5"/><text x="17" y="20" font-size="9" fill="#fff" text-anchor="middle" font-family="Arial, sans-serif">30</text></svg>
      <svg viewBox="0 0 34 28"><rect x="6" y="3" width="22" height="22" fill="none" stroke="#fff" stroke-width="1.5"/><circle cx="17" cy="14" r="7" fill="none" stroke="#fff" stroke-width="1.5"/></svg>
      <svg viewBox="0 0 34 28"><path d="M4 22 H30 L26 8 H12" fill="none" stroke="#fff" stroke-width="1.5"/></svg>
      <svg viewBox="0 0 34 28"><path d="M17 3 L31 25 H3 Z" fill="none" stroke="#fff" stroke-width="1.5"/><path d="M5 4 L29 26 M29 4 L5 26" stroke="#fff" stroke-width="1.5"/></svg>
    </div>
    <p class="coupon-offer"><b>50%</b>your first order</p>
    <p class="coupon-code">coupon code ROVK50</p>
    <p class="coupon-free">2nd order FREE!</p>
    <p class="coupon-cap">(up to $50)</p>
  </section>

  <div class="partner-badges" aria-hidden="true">
    <div class="badge badge-round-blue"></div>
    <div class="badge badge-round-sand"></div>
    <div class="badge badge-square"></div>
  </div>

  <p class="call-to-action">Schedule Your Pick Up Now And<br>Receive 50% Off Your First Order!</p>

  <div class="basket-art" role="img" aria-label="Illustration of a blue laundry basket filled with colourful clothes"></div>

  <p class="brand-name">brimfold.com</p>
  <p class="slogan">Cleaner. Brighter. Faster.</p>

  <p class="footer-line">SCHEDULE NOW ON WWW.BRIMFOLD.COM!</p>
</main>
</body>
</html>
```